Clara Joy Halden- Lantern Waltz- Autumn/Winter Tour Dates

I need high res A3 Tour poster for print and for social media JPG sharing of tour dates.
Also needed Facebook/Twitter Banner Cover Photos of these dates.
Text Needed Below
Clara Joy Halden
Lantern Waltz
Autumn/Winter Tour Dates
03/09 Ravensby Folk Festival
21/09 Swindon- Calder Theatre
01/10 Hitchin- Brackwell Folk Club
17/10 Bath- The Anvil
20/10 Sheffield- Upper Dale Croquet Club
24/10 Birmingham- Orchard Lamp Cafe
26/10 Glasgow- The Nook and Jar
27/10 Edinburgh - The Marble Parlour
08/11 Capital Reel and Ballad Festival- The Crooked Heron
25/11 Lewes- Tandem Record Shop- Live In Store
02/12 Cambridge- The Quayside
27/01 Lincolnshire- Fenmarsh Theatre
Tickets/Info: www.clarajoyhalden-music.example/gigs
(Quotes/Reviews To Put On)
"Outstanding, rich and expressive."            "Vibrant and Experimental"
**** BdM                                                               **** Tunepaths
"Impressive and Invigorating"                        "Enchanting" Acoustic Wire UK
tBarks

Updates
I cannot read the tour dates on most of the submissions so far. They need to be visible to viewers.
Thank You.
Please also be as creative and inventive as possible- not bland.

Target Market(s)
Music Fans- Folk Acoustic Americana
Industry/Entity Type
Media
Font styles to use
Requirements
Must have
- My photo featured prominently
- Look classy and not tacky or OTT
- Look elegant, wintery and eye catching
- The dates must be very clear to read
- Links to Website:

Nice to have
- Something innovative and not boring in terms of layout design
- Perhaps fading/ misty or wintery

Should not have
- Any colours that do not match

```html
<!DOCTYPE html>
<html lang="en">
<head>
<meta charset="utf-8">
<title>Clara Joy Halden – Autumn / Winter Tour Dates</title>
<link rel="stylesheet" href="https://fonts.googleapis.com/css2?family=Cinzel:wght@400;600&family=Cinzel+Decorative:wght@400;700&family=Rajdhani:wght@600;700&display=swap">
<style>
  :root {
    --navy-deep: #050d22;
    --navy: #0b1d42;
    --blue: #1d4688;
    --blue-glow: #3f7cc8;
    --mist: #8fb6e6;
    --hair: #04060d;
    --skin-tone: #b9bfd3;
    --white: #f3f6fb;
    --date-grey: #c9d3e4;
    --band: #060b18;
  }
  * { margin: 0; padding: 0; box-sizing: border-box; }
  html, body {
    width: 950px; height: 1200px; overflow: hidden;
    background: var(--navy-deep);
  }
  .poster {
    position: relative; width: 950px; height: 1200px; overflow: hidden;
    color: var(--white);
    background: linear-gradient(180deg, var(--navy) 0%, #0a1838 22%, #163a78 60%, #12306a 78%, var(--navy-deep) 100%);
  }
  .poster-photo {
    position: absolute; left: 0; right: 0; top: 230px; height: 600px;
    background:
      radial-gradient(ellipse 9% 13% at 50% 54%, var(--skin-tone) 0%, #7d86a3 55%, rgba(60,70,100,0) 100%),
      radial-gradient(ellipse 46% 42% at 50% 36%, var(--hair) 0%, rgba(4,6,13,.92) 45%, rgba(4,6,13,0) 100%),
      radial-gradient(ellipse 20% 10% at 50% 82%, #2b4f8f 0%, rgba(43,79,143,0) 100%),
      radial-gradient(ellipse 70% 55% at 50% 70%, #2f63b0 0%, rgba(47,99,176,0) 80%),
      linear-gradient(180deg, rgba(11,29,66,0) 0%, #14336f 45%, #1f4a92 80%, rgba(29,70,136,0) 100%);
    -webkit-mask-image: linear-gradient(180deg, transparent 0%, #000 14%, #000 82%, transparent 100%);
    mask-image: linear-gradient(180deg, transparent 0%, #000 14%, #000 82%, transparent 100%);
  }
  .poster-mist {
    position: absolute; inset: 0; pointer-events: none;
    background:
      radial-gradient(ellipse 55% 12% at 50% 3%, rgba(63,124,200,.35), transparent 70%),
      radial-gradient(ellipse 25% 9% at 6% 66%, rgba(63,124,200,.35), transparent 70%),
      radial-gradient(ellipse 25% 9% at 94% 66%, rgba(63,124,200,.35), transparent 70%);
  }
  .headline { position: absolute; top: 30px; left: 0; right: 0; text-align: center; }
  .artist-name {
    font-family: "Cinzel Decorative", serif; font-weight: 400;
    font-size: 80px; letter-spacing: 1px; line-height: 1;
    text-shadow: 0 0 14px rgba(143,182,230,.45);
  }
  .title-rule { display: block; margin: 20px auto 0; width: 800px; height: 4px; }
  .review-quote {
    margin-top: 12px;
    font-family: "Cinzel", serif; font-size: 33px; letter-spacing: .5px;
    text-transform: uppercase; font-weight: 400;
  }
  .album-title {
    margin-top: 14px;
    font-family: "Cinzel Decorative", serif; font-weight: 400; font-size: 38px; letter-spacing: 1px;
  }
  .tour-heading {
    position: absolute; top: 792px; left: 0; right: 0; text-align: center;
    font-family: "Cinzel Decorative", serif; font-weight: 400; font-size: 35px;
    text-shadow: 0 0 10px rgba(143,182,230,.5);
  }
  .tour-dates {
    position: absolute; top: 848px; left: 42px; right: 30px;
    display: grid; grid-template-columns: 430px 1fr;
    font-family: "Rajdhani", sans-serif; font-weight: 700; font-size: 18.5px;
  }
  .tour-column { list-style: none; }
  .tour-column + .tour-column {
    border-left: 1px solid rgba(143,182,230,.35); padding-left: 18px;
  }
  .gig { display: flex; height: 32.5px; align-items: center; }
  .gig-date { width: 65px; flex: none; color: var(--date-grey); }
  .gig-venue { color: var(--white); }
  .gig-continued { padding-left: 65px; }
  .tickets-band {
    position: absolute; top: 1088px; left: 10px; right: 10px; height: 38px;
    background: var(--band);
    display: flex; align-items: center; justify-content: center; gap: 12px;
  }
  .tickets-label { font-family: "Cinzel", serif; font-size: 17px; letter-spacing: 1px; }
  .tickets-url {
    font-family: "Cinzel", serif; font-weight: 600; font-size: 21px; letter-spacing: .5px;
    text-transform: uppercase;
  }
  .social-row {
    position: absolute; top: 1140px; left: 0; right: 0;
    display: flex; justify-content: center; gap: 36px;
    font-family: "Cinzel", serif; font-size: 15px; color: var(--date-grey);
  }
  .social-handle { display: flex; align-items: center; gap: 10px; }
  .social-dot { width: 24px; height: 24px; border-radius: 50%; background: var(--date-grey); }
</style>
</head>
<body>
<main class="poster">
  <div class="poster-photo" role="img" aria-label="Photo of the singer lying upside down, long dark hair spread across a deep blue starry backdrop with strands of small glass beads around her"></div>
  <div class="poster-mist"></div>

  <header class="headline">
    <h1 class="artist-name">Clara Joy Halden</h1>
    <svg class="title-rule" viewBox="0 0 800 4" preserveAspectRatio="none" aria-hidden="true">
      <defs>
        <linearGradient id="rule-fade" x1="0" x2="1">
          <stop offset="0" stop-color="#f3f6fb" stop-opacity="0"/>
          <stop offset=".5" stop-color="#f3f6fb"/>
          <stop offset="1" stop-color="#f3f6fb" stop-opacity="0"/>
        </linearGradient>
      </defs>
      <rect width="800" height="4" fill="url(#rule-fade)"/>
    </svg>
    <p class="review-quote">Outstanding, rich and expressive</p>
    <h2 class="album-title">Lantern Waltz</h2>
  </header>

  <h3 class="tour-heading">Autumn / Winter Tour Dates</h3>

  <section class="tour-dates">
    <ul class="tour-column">
      <li class="gig"><span class="gig-date">03/09 -</span><span class="gig-venue">Ravensby Folk Festival</span></li>
      <li class="gig"><span class="gig-date">21/09 -</span><span class="gig-venue">Swindon- Calder Theatre</span></li>
      <li class="gig"><span class="gig-date">01/10 -</span><span class="gig-venue">Hitchin- Brackwell Folk Club</span></li>
      <li class="gig"><span class="gig-date">17/10 -</span><span class="gig-venue">Bath- The Anvil</span></li>
      <li class="gig"><span class="gig-date">20/10 -</span><span class="gig-venue">Sheffield- Upper Dale Croquet Club</span></li>
      <li class="gig"><span class="gig-date">24/10 -</span><span class="gig-venue">Birmingham- Orchard Lamp Cafe</span></li>
      <li class="gig"><span class="gig-date">26/10 -</span><span class="gig-venue">Glasgow- The Nook and Jar</span></li>
    </ul>
    <ul class="tour-column">
      <li class="gig"><span class="gig-date">27/10 -</span><span class="gig-venue">Edinburgh - The Marble Parlour</span></li>
      <li class="gig"><span class="gig-date">08/11 -</span><span class="gig-venue">Capital Reel and Ballad Festival-</span></li>
      <li class="gig gig-continued"><span class="gig-venue">The Crooked Heron</span></li>
      <li class="gig"><span class="gig-date">25/11 -</span><span class="gig-venue">Lewes- Tandem Record Shop- Live In Store</span></li>
      <li class="gig"><span class="gig-date">02/12 -</span><span class="gig-venue">Cambridge- The Quayside</span></li>
      <li class="gig"><span class="gig-date">27/01 -</span><span class="gig-venue">Lincolnshire- Fenmarsh Theatre</span></li>
    </ul>
  </section>

  <div class="tickets-band">
    <span class="tickets-label">TICKETS/INFO:</span>
    <span class="tickets-url">www.clarajoyhalden-music.example/gigs</span>
  </div>

  <footer class="social-row">
    <span class="social-handle"><span class="social-dot"></span>/ClaraJoyHaldenmusic</span>
    <span class="social-handle"><span class="social-dot"></span>/ClaraJoyHalden</span>
  </footer>
</main>
</body>
</html>
```